Redesign of Business Cards to Update them!

We want a full overhaul of our business cards! We have a design that is almost 5 years old and it needs to be updated to be current

Address is 437 Dunmore Lane Suite C San Bernardino CA 92408
PH: 9094718263
Zorlivo.com

Hours M-F 10AM-4PM
Sat and Sunday Closed

```html
<!DOCTYPE html>
<html lang="en">
<head>
<meta charset="utf-8">
<title>Zorlivo Business Card</title>
<link href="https://fonts.googleapis.com/css2?family=Montserrat:wght@400;500;800&display=swap" rel="stylesheet">
<style>
  :root {
    --backdrop: #2a2a2a;
    --brand-red: #f20a0a;
    --brand-red-light: #ff2a2a;
    --ink: #111111;
    --paper: #ffffff;
  }
  html, body {
    margin: 0;
    padding: 0;
    width: 1200px;
    height: 881px;
    overflow: hidden;
    background: var(--backdrop);
    font-family: "Montserrat", Arial, sans-serif;
  }
  .canvas {
    position: relative;
    width: 1200px;
    height: 881px;
  }
  .card {
    position: absolute;
    left: 250px;
    width: 700px;
    height: 400px;
    border-radius: 26px;
    overflow: hidden;
  }
  .card--front {
    top: 28px;
    background: linear-gradient(135deg, var(--brand-red-light) 0%, var(--brand-red) 60%, #e00000 100%);
  }
  .card--back {
    top: 453px;
    background: var(--paper);
  }

  /* brand block */
  .brand {
    position: absolute;
    display: flex;
    flex-direction: column;
    align-items: center;
  }
  .brand__art {
    width: 240px;
    height: 110px;
    border-radius: 14px;
  }
  .brand__name {
    margin-top: 14px;
    font-weight: 800;
    font-size: 56px;
    letter-spacing: 1px;
    color: var(--ink);
    line-height: 1;
  }
  .card--front .brand { left: 210px; top: 105px; }
  .card--front .brand__art {
    background: linear-gradient(90deg, #ffffff 0%, #ffd6d6 50%, #ffffff 100%);
    opacity: 0.9;
  }
  .card--back .brand { left: 60px; top: 110px; }
  .card--back .brand__art {
    background: linear-gradient(90deg, var(--brand-red) 0%, #ff6a6a 50%, var(--brand-red) 100%);
  }

  /* contact block */
  .contact {
    position: absolute;
    left: 400px;
    top: 95px;
    width: 270px;
  }
  .contact__hours {
    margin: 0;
    color: var(--brand-red);
    font-weight: 500;
    font-size: 15px;
    line-height: 1.35;
    text-transform: uppercase;
  }
  .contact__rule {
    margin: 12px 0 14px;
    border: 0;
    border-top: 1.5px solid var(--brand-red);
  }
  .contact__line {
    margin: 0 0 6px;
    font-size: 15px;
    color: var(--ink);
  }
  .contact__label {
    color: var(--brand-red);
    font-weight: 800;
    margin-right: 4px;
  }

  .wave {
    position: absolute;
    left: 0;
    bottom: 0;
    width: 700px;
    height: 170px;
  }
</style>
</head>
<body>
<main class="canvas">

  <section class="card card--front">
    <div class="brand">
      <div class="brand__art" role="img" aria-label="Mascot illustration: sad character with broken phone, arrow, happy character with repaired phone"></div>
      <div class="brand__name">Zorlivo</div>
    </div>
  </section>

  <section class="card card--back">
    <div class="brand">
      <div class="brand__art" role="img" aria-label="Mascot illustration: sad character with broken phone, arrow, happy character with repaired phone"></div>
      <div class="brand__name">Zorlivo</div>
    </div>

    <div class="contact">
      <p class="contact__hours">Hours M-F 10AM-4PM<br>Sat and Sunday Closed</p>
      <hr class="contact__rule">
      <p class="contact__line"><span class="contact__label">P</span>: 9094718263</p>
      <p class="contact__line"><span class="contact__label">W</span>: www.zorlivo.com</p>
    </div>

    <svg class="wave" viewBox="0 0 700 170" preserveAspectRatio="none" aria-hidden="true">
      <path d="M0 150 C 220 150, 360 20, 700 40 L700 170 L0 170 Z" fill="var(--brand-red)"/>
      <path d="M0 142 C 220 144, 360 12, 700 30" fill="none" stroke="var(--ink)" stroke-width="6"/>
    </svg>
  </section>

</main>
</body>
</html>
```